Copper Lantern

Please see attached Word document for requirements. I want the website to be one page.

Coding

Coded - Design and coding required

Number of Pages Required

1 page

Colors
0054AA
0677BA
7BADD7
CADEEF
E8F1F8

```html
<!DOCTYPE html>
<html lang="en">
<head>
<meta charset="utf-8">
<title>Copper Lantern – Smarter Workforce Scheduling</title>
<link href="https://fonts.googleapis.com/css2?family=Montserrat:wght@400;500;600;700;800&family=Poppins:wght@400;500;600&display=swap" rel="stylesheet">
<style>
:root{
  --navy:#0a3a8c;
  --blue:#0054AA;
  --blue-2:#0677BA;
  --blue-3:#7BADD7;
  --blue-4:#CADEEF;
  --blue-5:#E8F1F8;
  --ink:#111827;
  --text:#374151;
  --muted:#6b7280;
  --white:#ffffff;
  --line:#d6dde6;
}
*{margin:0;padding:0;box-sizing:border-box}
html,body{width:1200px;height:4728px;overflow:hidden}
body{font-family:"Poppins",sans-serif;color:var(--text);background:var(--white);position:relative}
.abs{position:absolute}
h1,h2,h3,h4{font-family:"Montserrat",sans-serif;color:var(--ink)}
.brand{font-family:"Poppins",sans-serif;font-weight:600;color:#5b6478;display:flex;align-items:center;gap:8px;white-space:nowrap}
.brand .dot{width:12px;height:12px;border-radius:50%;background:var(--blue-3);flex:none}
.btn{display:inline-flex;align-items:center;gap:10px;height:36px;padding:0 8px 0 12px;font:600 14px "Montserrat",sans-serif;color:#fff;background:var(--blue);border-radius:2px;white-space:nowrap}
.btn .arr{width:22px;height:22px;background:#fff;color:var(--blue);display:flex;align-items:center;justify-content:center;font-size:12px}
.btn.light{background:var(--blue-3)}

/* top bar */
.topbar{left:0;top:0;width:1200px;height:40px;background:var(--navy);color:#fff;font-size:14px}
.topbar span{position:absolute;top:10px}
.nav{left:79px;top:66px;width:1038px;height:77px;background:#fff;border-radius:6px;box-shadow:0 4px 18px rgba(10,40,100,.12)}
.nav .brand{position:absolute;left:32px;top:22px;font-size:26px}
.nav ul{position:absolute;left:415px;top:26px;list-style:none;display:flex;gap:38px;font:500 17px "Montserrat",sans-serif;color:var(--ink)}
.nav ul li.on{border-bottom:2px solid var(--blue);padding-bottom:6px}
.nav .btn{position:absolute;right:30px;top:20px}

/* hero */
.hero-bg{left:0;top:40px;width:1200px;height:890px;background:linear-gradient(180deg,#f3f7fc 0%,#e2ecf8 45%,#b6d0ee 100%)}
.hero-curve{left:0;top:700px;width:1200px;height:230px}
.hero h1{position:absolute;left:0;width:1200px;text-align:center}
.hero .t1{top:198px;font-size:51px;font-weight:800}
.hero .t2{top:251px;font-size:51px;font-weight:500}
.hero p{position:absolute;top:314px;width:1200px;text-align:center;font-size:18px;color:var(--ink)}
.hero .b1{left:426px;top:355px}
.hero .b2{left:606px;top:355px}
.dash{left:259px;top:428px;width:693px;height:480px;background:var(--blue);border-radius:12px;padding:48px 55px 0 50px}
.dash .screen{width:100%;height:100%;background:linear-gradient(180deg,#eef1f8,#dfe5f1);border-radius:4px 4px 0 0}

/* why */
.sec-title{position:absolute;left:0;width:1200px;text-align:center;font-size:36px;font-weight:500}
.sec-title b{font-weight:700}
.rule{position:absolute;left:560px;width:80px;height:3px;background:var(--blue)}
.why-card{top:1138px;width:220px;height:229px;border:1px solid var(--line);border-radius:6px;text-align:center;background:#fff}
.icon-c{position:absolute;width:72px;height:72px;border-radius:50%;background:var(--blue);border:4px solid #dbe7f5;display:flex;align-items:center;justify-content:center}
.why-card .icon-c{left:74px;top:-36px}
.why-card h3{margin-top:52px;font-size:17px;font-weight:700;line-height:26px}
.why-card p{margin:12px 14px 0;font-size:13px;line-height:19px;color:var(--muted)}

/* features */
.features{left:0;top:1464px;width:1200px;height:595px;background:var(--blue-5);overflow:hidden}
.feat{position:absolute;font-size:14px;line-height:24px;color:var(--text)}
.feat h4{font-size:18px;font-weight:700;margin-bottom:4px}
.features .icon-c{width:62px;height:62px}
.center-mark{left:411px;top:440px;width:360px;justify-content:center;font-size:34px}

/* industries */
.industries{left:0;top:2059px;width:1200px;height:613px;background:linear-gradient(180deg,#1a4aa3,#0b45b5)}
.ind-card{top:169px;width:222px;height:295px;background:#fff;border-radius:2px;text-align:center}
.ind-card .ph{height:190px}
.ind-card .icon-c{left:75px;top:154px}
.ind-card h4{margin-top:54px;font-size:17px;font-weight:700}
.ind-card p{margin:12px 12px 0;font-size:13px;line-height:23px;color:var(--ink)}

/* testimonials */
.t-card{background:#fff;box-shadow:0 8px 30px rgba(0,0,0,.08);border-radius:4px}
.t-card.side{background:#f2f2f2;box-shadow:none}
.avatar{position:absolute;border-radius:50%;background:linear-gradient(135deg,#c69c7c,#7a5a44);border:3px solid #fff}
.t-name{position:absolute;font:700 13px "Montserrat",sans-serif;color:var(--ink)}
.stars{color:#e06a1b;margin-left:14px;letter-spacing:2px}
.t-card p{position:absolute;font-size:11px;line-height:22px;color:var(--muted)}
.dots{left:558px;top:3142px;display:flex;gap:6px}
.dots i{width:12px;height:12px;border-radius:50%;background:var(--blue-4)}
.dots i:first-child{background:var(--blue)}

/* pricing */
.pricing{left:0;top:3230px;width:1200px;height:807px;background:var(--blue-5)}
.plan{background:#fff;box-shadow:0 6px 20px rgba(0,0,0,.08)}
.plan .head{position:absolute;left:0;top:0;width:100%;background:var(--blue);text-align:center}
.plan .head h3{color:#fff;font-size:31px;font-weight:600}
.price{position:absolute;border-radius:50%;background:#fff;border:5px solid var(--navy);display:flex;align-items:center;justify-content:center;font:700 31px "Montserrat",sans-serif;color:var(--navy)}
.plan ul{position:absolute;left:30px;list-style:none;font-size:16px;color:var(--ink)}
.plan li::before{content:"✔";color:var(--blue-2);margin-right:14px}
.plan .more{position:absolute;left:0;width:100%;text-align:center;font:600 18px "Montserrat",sans-serif;color:var(--blue)}
.plan .dash-line{position:absolute;left:8px;right:8px;border-top:2px dashed #cfd6df}

/* cta */
.cta{left:112px;top:4037px;width:974px;height:297px;background:linear-gradient(180deg,#2a62bd,#1f57b6)}
.cta h2{position:absolute;top:80px;width:100%;text-align:center;color:#fff;font-size:31px;font-weight:400}
.cta h2 b{font-weight:700}

/* footer */
.footer .brand{font-size:30px}
.vline{width:3px;height:46px;background:var(--blue)}
.f-title{font:600 15px "Montserrat",sans-serif;color:var(--ink)}
.f-link{font-size:13px;color:#4b5563}
.social{width:30px;height:30px;border-radius:50%;border:1px solid #aab4c2}
</style>
</head>
<body>

<div class="abs topbar">
  <span style="left:110px">☏&nbsp; Call Us Now: +1 555 010 0199</span>
  <span style="left:800px">👤 Log In</span>
  <span style="left:916px">✆ Customer Support</span>
</div>

<div class="abs hero-bg"></div>
<svg class="abs hero-curve" viewBox="0 0 1200 230">
  <path d="M0 162 C0 60 70 16 260 16 L940 16 C1130 16 1200 60 1200 162 L1200 230 L0 230 Z" fill="#fff"/>
</svg>

<div class="abs nav">
  <div class="brand"><span class="dot"></span>Copper Lantern</div>
  <ul><li class="on">Home</li><li>Features</li><li>Pricing</li><li>Contact</li></ul>
  <span class="btn">Demo Booking <span class="arr">›</span></span>
</div>

<section class="hero">
  <h1 class="t1">Smarter Workforce Scheduling,</h1>
  <h1 class="t2">Automatically.</h1>
  <p>Automate rosters, reduce costs, and ensure compliance — all in one platform.</p>
  <span class="btn abs b1">Start Free Trial <span class="arr">›</span></span>
  <span class="btn light abs b2">Book a Demo <span class="arr">›</span></span>
</section>

<div class="abs dash"><div class="screen" role="img" aria-label="Scheduling dashboard preview with order stats, shipment bar chart and order list"></div></div>

<h2 class="sec-title" style="top:993px">Why <b>Copper Lantern</b> is different</h2>
<div class="rule" style="top:1056px"></div>

<div class="abs why-card" style="left:114px">
  <div class="icon-c"><svg width="30" height="30" viewBox="0 0 24 24" fill="none" stroke="#fff" stroke-width="1.6"><rect x="4" y="3" width="16" height="18" rx="2"/><path d="M8 15l3-3 2 2 3-4"/></svg></div>
  <h3>Intelligent<br>Automation</h3>
  <p>Create scouting reports using a structured evaluation framework that ensures consistency across all reports.</p>
</div>
<div class="abs why-card" style="left:367px">
  <div class="icon-c"><svg width="30" height="30" viewBox="0 0 24 24" fill="none" stroke="#fff" stroke-width="1.6"><rect x="4" y="3" width="16" height="18" rx="2"/><path d="M8 8h8M8 12h8M8 16h5"/></svg></div>
  <h3>Cost<br>Optimisation</h3>
  <p>Create scouting reports using a structured evaluation framework that ensures consistency across all reports.</p>
</div>
<div class="abs why-card" style="left:620px">
  <div class="icon-c"><svg width="30" height="30" viewBox="0 0 24 24" fill="none" stroke="#fff" stroke-width="1.6"><rect x="5" y="4" width="14" height="17" rx="2"/><path d="M9 4V2h6v2M8 10h8M8 14h8"/></svg></div>
  <h3>Fair &amp; Compliant<br>Scheduling</h3>
  <p>Create scouting reports using a structured evaluation framework that ensures consistency across all reports.</p>
</div>
<div class="abs why-card" style="left:873px">
  <div class="icon-c"><svg width="30" height="30" viewBox="0 0 24 24" fill="none" stroke="#fff" stroke-width="1.6"><circle cx="12" cy="12" r="9"/><path d="M3 12h18M12 3c3 3 3 15 0 18M12 3c-3 3-3 15 0 18"/></svg></div>
  <h3>Multi-Site<br>Flexibility</h3>
  <p>Create scouting reports using a structured evaluation framework that ensures consistency across all reports.</p>
</div>

<section class="abs features">
  <h2 class="sec-title" style="top:78px">Features <span style="font-weight:500">Overview</span></h2>
  <div class="rule" style="top:130px"></div>
  <svg class="abs" style="left:0;top:0" width="1200" height="595">
    <path d="M370 595 L370 495 A220 220 0 0 1 810 495 L810 595" fill="none" stroke="#0a3a8c" stroke-width="2" stroke-dasharray="6 5"/>
    <circle cx="591" cy="492" r="180" fill="#f1f1f1"/>
  </svg>
  <div class="brand abs center-mark"><span class="dot" style="width:14px;height:14px"></span>Copper Lantern</div>

  <div class="icon-c" style="left:560px;top:245px"><svg width="26" height="26" viewBox="0 0 24 24" fill="none" stroke="#fff" stroke-width="1.6"><path d="M4 20h16M6 20V9h12v11M9 13h2M13 13h2M12 9V5"/></svg></div>
  <div class="icon-c" style="left:395px;top:305px"><svg width="26" height="26" viewBox="0 0 24 24" fill="none" stroke="#fff" stroke-width="1.6"><path d="M5 4l4 1 1 4-2 2a11 11 0 005 5l2-2 4 1 1 4c-9 1-16-6-15-15z"/></svg></div>
  <div class="icon-c" style="left:721px;top:309px"><svg width="26" height="26" viewBox="0 0 24 24" fill="none" stroke="#fff" stroke-width="1.6"><path d="M6 4v12h6M18 20V8h-6"/></svg></div>
  <div class="icon-c" style="left:332px;top:441px"><svg width="26" height="26" viewBox="0 0 24 24" fill="none" stroke="#fff" stroke-width="1.6"><rect x="4" y="4" width="14" height="17" rx="2"/><path d="M8 9h6M8 13h6M8 17h3"/></svg></div>
  <div class="icon-c" style="left:778px;top:441px"><svg width="26" height="26" viewBox="0 0 24 24" fill="none" stroke="#fff" stroke-width="1.6"><circle cx="12" cy="12" r="8"/><circle cx="12" cy="12" r="4"/></svg></div>

  <div class="feat" style="left:420px;top:160px;width:340px;text-align:center"><h4>Cost optimisation</h4>Specialized solutions for<br>commercial and industrial system</div>
  <div class="feat" style="left:100px;top:290px;width:273px;text-align:right"><h4>Compliance engine</h4>Fast response anytime to minimize downtime and damage.</div>
  <div class="feat" style="left:804px;top:290px;width:270px"><h4>Multi-site support</h4>Specialized solutions for commercial and industrial system</div>
  <div class="feat" style="left:50px;top:425px;width:265px;text-align:right"><h4>Automated scheduling</h4>Regular inspections to prevent costly plumbing failures.</div>
  <div class="feat" style="left:863px;top:425px;width:300px"><h4>Staff self-service</h4>Supporting businesses across California with dependable service.</div>
</section>

<section class="abs industries">
  <h2 class="sec-title" style="top:70px;color:#fff"><b>Industries</b> Served</h2>
  <div class="rule" style="top:121px;background:#fff"></div>
  <div class="abs ind-card" style="left:114px">
    <div class="ph" role="img" aria-label="Photo of a white hard hat on site plans" style="background:linear-gradient(160deg,#c9d6e6,#6f87a6)"></div>
    <div class="icon-c"><svg width="28" height="28" viewBox="0 0 24 24" fill="none" stroke="#fff" stroke-width="1.8"><circle cx="12" cy="12" r="7"/><path d="M9 12l2 2 4-4"/></svg></div>
    <h4>HEALTHCARE</h4>
  </div>
  <div class="abs ind-card" style="left:363px;top:165px;width:226px;height:353px;border:2px solid #b8c4d6">
    <div class="ph" role="img" aria-label="Photo of engineers in hi-vis vests reviewing plans" style="background:linear-gradient(160deg,#8a9aa8,#4d5e6e)"></div>
    <div class="icon-c" style="left:76px"><svg width="28" height="28" viewBox="0 0 24 24" fill="none" stroke="#fff" stroke-width="1.8"><path d="M5 10h14l-2 10H7zM9 10V6h6v4"/></svg></div>
    <h4>HOSPITALITY</h4>
    <p>Streamlined collaboration from concept to completion.</p>
  </div>
  <div class="abs ind-card" style="left:617px">
    <div class="ph" role="img" aria-label="Photo of workers in orange suits on a rail track" style="background:linear-gradient(160deg,#7b7b78,#3e3c3a)"></div>
    <div class="icon-c"><svg width="28" height="28" viewBox="0 0 24 24" fill="none" stroke="#fff" stroke-width="1.8"><path d="M4 20h16M7 20v-6h10v6M12 14V6l4 3"/></svg></div>
    <h4>LOGISTICS</h4>
  </div>
  <div class="abs ind-card" style="left:868px">
    <div class="ph" role="img" aria-label="Photo of an industrial plant with pipes and workers" style="background:linear-gradient(160deg,#b9c2c8,#6b6e60)"></div>
    <div class="icon-c"><svg width="28" height="28" viewBox="0 0 24 24" fill="none" stroke="#fff" stroke-width="1.8"><circle cx="12" cy="12" r="3"/><circle cx="12" cy="12" r="8" stroke-dasharray="4 3"/></svg></div>
    <h4>MANUFACTURING</h4>
  </div>
</section>

<h2 class="sec-title" style="top:2742px">Client <span style="font-weight:500">Testimonials</span></h2>
<div class="rule" style="top:2796px"></div>

<div class="abs t-card side" style="left:50px;top:2885px;width:328px;height:183px">
  <p style="left:26px;top:54px;width:284px">Lorem ipsum dolor sit amet, consectetur adipiscing elit, sed do eiusmod tempor incididunt ut labore et dolore magna aliqua. Ut enim ad minim veniam, quis nostrud exercitation ullamco laboris nisi ut aliquip ex ea commodo consequat.</p>
</div>
<div class="avatar abs" role="img" aria-label="Client portrait" style="left:74px;top:2862px;width:60px;height:60px"></div>
<div class="t-name" style="left:152px;top:2900px">ELENA MARSH<span class="stars">★★★★★</span></div>

<div class="abs t-card" style="left:398px;top:2866px;width:411px;height:232px">
  <p style="left:32px;top:64px;width:350px;font-size:13px;line-height:25px">Lorem ipsum dolor sit amet, consectetur adipiscing elit, sed do eiusmod tempor incididunt ut labore et dolore magna aliqua. Ut enim ad minim veniam, quis nostrud exercitation ullamco laboris nisi ut aliquip ex ea commodo consequat.</p>
</div>
<div class="avatar abs" role="img" aria-label="Client portrait" style="left:428px;top:2838px;width:74px;height:74px"></div>
<div class="t-name" style="left:526px;top:2886px;font-size:14px">ELENA MARSH<span class="stars">★★★★★</span></div>

<div class="abs t-card side" style="left:830px;top:2885px;width:328px;height:183px">
  <p style="left:26px;top:54px;width:284px">Lorem ipsum dolor sit amet, consectetur adipiscing elit, sed do eiusmod tempor incididunt ut labore et dolore magna aliqua. Ut enim ad minim veniam, quis nostrud exercitation ullamco laboris nisi ut aliquip ex ea commodo consequat.</p>
</div>
<div class="avatar abs" role="img" aria-label="Client portrait" style="left:854px;top:2862px;width:60px;height:60px"></div>
<div class="t-name" style="left:930px;top:2900px">ELENA MARSH<span class="stars">★★★★★</span></div>

<div class="abs dots"><i></i><i></i><i></i><i></i><i></i></div>

<section class="abs pricing">
  <h2 class="sec-title" style="top:86px">Our <b>Pricing</b></h2>

  <div class="abs plan" style="left:99px;top:205px;width:314px;height:477px">
    <div class="head" style="height:140px"><h3 style="margin-top:26px">Starter</h3></div>
    <div class="price" style="left:104px;top:83px;width:106px;height:106px">$15</div>
    <ul style="top:222px"><li style="height:40px">Lorem ipsum dolor sit</li><li style="height:40px">Duis aute irure dolor</li><li style="height:40px">Sed ut perspiciatis unde</li><li>Neque porro quisquam</li></ul>
    <div class="dash-line" style="top:400px"></div>
    <div class="more" style="top:425px">View Details »</div>
  </div>

  <div class="abs plan" style="left:785px;top:205px;width:312px;height:477px">
    <div class="head" style="height:140px"><h3 style="margin-top:26px">Enterprise</h3></div>
    <div class="price" style="left:103px;top:83px;width:106px;height:106px">$12</div>
    <ul style="top:222px"><li style="height:40px">Lorem ipsum dolor sit</li><li style="height:40px">Duis aute irure dolor</li><li style="height:40px">Sed ut perspiciatis unde</li><li>Neque porro quisquam</li></ul>
    <div class="dash-line" style="top:400px"></div>
    <div class="more" style="top:425px">View Details »</div>
  </div>

  <div class="abs plan" style="left:413px;top:178px;width:372px;height:526px;box-shadow:0 10px 30px rgba(0,0,0,.14)">
    <div class="head" style="height:167px;background:var(--navy)"><h3 style="margin-top:28px">Professional</h3></div>
    <div class="price" style="left:126px;top:94px;width:120px;height:120px;font-size:34px">$152</div>
    <ul style="top:250px;left:38px;font-size:17px"><li style="height:45px">Lorem ipsum dolor sit</li><li style="height:45px">Duis aute irure dolor</li><li style="height:45px">Sed ut perspiciatis unde</li><li>Neque porro quisquam</li></ul>
    <div class="more" style="top:474px">View Details »</div>
  </div>
</section>

<section class="abs cta">
  <h2>Ready to transform <b>your workforce?</b></h2>
  <span class="btn abs" style="left:296px;top:168px">Start Free Trial <span class="arr">›</span></span>
  <span class="btn light abs" style="left:476px;top:168px">Free Trial Sign-ups <span class="arr">›</span></span>
</section>

<footer class="footer">
  <div class="brand abs" style="left:112px;top:4470px"><span class="dot"></span>Copper Lantern</div>
  <div class="abs vline" style="left:413px;top:4426px"></div>
  <div class="abs vline" style="left:759px;top:4426px"></div>
  <div class="abs f-title" style="left:492px;top:4426px">QUICK LINKS</div>
  <div class="abs f-link" style="left:492px;top:4468px;line-height:25px">Home<br>Services<br>About Us<br>Testimonials<br>Contact</div>
  <div class="abs f-link" style="left:629px;top:4468px;line-height:25px">Support<br>Blog<br>Imprint<br>Careers</div>
  <div class="abs f-title" style="left:824px;top:4426px">CONTACT INFO</div>
  <svg class="abs" style="left:826px;top:4470px" width="14" height="18" viewBox="0 0 14 18"><path d="M7 1a6 6 0 016 6c0 4-6 10-6 10S1 11 1 7a6 6 0 016-6z" fill="none" stroke="#0054AA" stroke-width="1.6"/><circle cx="7" cy="7" r="2" fill="#0054AA"/></svg>
  <div class="abs f-link" style="left:855px;top:4468px;line-height:24px;color:var(--ink)">48 Harbor Lane, Dallas,<br>TX 75201</div>
  <svg class="abs" style="left:824px;top:4535px" width="18" height="13" viewBox="0 0 18 13"><rect x="1" y="1" width="16" height="11" fill="none" stroke="#0054AA" stroke-width="1.5"/><path d="M1 1l8 6 8-6" fill="none" stroke="#0054AA" stroke-width="1.5"/></svg>
  <div class="abs f-link" style="left:855px;top:4532px;color:var(--ink)">support@copperlantern.example</div>
  <svg class="abs" style="left:825px;top:4574px" width="16" height="16" viewBox="0 0 24 24"><path d="M5 3l4 1 1 4-2 2a11 11 0 006 6l2-2 4 1 1 4C12 20 4 12 5 3z" fill="none" stroke="#0054AA" stroke-width="2"/></svg>
  <div class="abs f-link" style="left:855px;top:4574px;color:var(--ink);text-decoration:underline">+1 555 010 0199</div>

  <div class="abs f-link" style="left:110px;top:4653px;color:var(--ink)">© 2026 Company Name. All Rights Reserved.</div>
  <div class="abs social" style="left:545px;top:4648px"></div>
  <div class="abs social" style="left:583px;top:4648px"></div>
  <div class="abs social" style="left:622px;top:4648px"></div>
  <div class="abs f-link" style="left:864px;top:4653px;color:var(--ink)">Privacy &nbsp;&nbsp;|&nbsp;&nbsp; Terms &nbsp;&nbsp;|&nbsp;&nbsp; Disclaimer</div>
</footer>

</body>
</html>
```